Business Card for my New Brokerage

Looking to get a business card design for my new Real Estate Brokerage.
I want it with Picture, Phone Number, Email, Website, Office Address
Name and Designation. Please add logo too.

Target Market(s)

Real Estate Investors or Home Buyers

Industry/Entity Type

Real Estate

Contact Information for Business Card

Name, Email, Phone Number, website, email, office address

Colors
EB3D1F
EC4F4E
F09395
F8D3D4
FCEDEE

Requirements
Must have
• Minimalistic, Clean, Modern, Photo
Nice to have
• White and Red Colors

```html
<!DOCTYPE html>
<html lang="en">
<head>
<meta charset="utf-8">
<title>Ember Realty Co — Business Card</title>
<link rel="stylesheet" href="https://fonts.googleapis.com/css2?family=Montserrat:wght@400;500;700;800&display=swap">
<style>
  :root {
    --red: #e2382a;
    --red-soft: #ec4f4e;
    --pink: #f09395;
    --blush: #f8d3d4;
    --cream: #fcedee;
    --white: #ffffff;
    --ink: #2b2b2b;
    --page: #eeeeee;
    --skyline: #eceded;
  }
  * { box-sizing: border-box; margin: 0; padding: 0; }
  html, body {
    width: 1187px; height: 1200px; overflow: hidden;
    background: var(--page);
    font-family: "Montserrat", Arial, sans-serif;
  }
  .canvas { position: relative; width: 1187px; height: 1200px; }

  /* Front of card */
  .card-front {
    position: absolute; left: 217px; top: 121px; width: 753px; height: 431px;
    background: var(--red);
    color: var(--white);
  }
  .card-front .pattern {
    position: absolute; inset: 0;
    background: radial-gradient(circle at 50% 50%, #e6473a 0%, var(--red) 70%);
  }
  .brand-front {
    position: absolute; left: 0; right: 0; top: 172px;
    text-align: center; font-weight: 700; line-height: 1;
  }
  .brand-front .brand-main { display: block; font-size: 86px; letter-spacing: 1px; }
  .brand-front .brand-sub { display: block; font-size: 26px; letter-spacing: 7px; margin-top: 12px; padding-left: 7px; }
  .front-url {
    position: absolute; left: 0; right: 0; top: 355px;
    text-align: center; font-size: 17px; font-weight: 500; letter-spacing: 1.2px;
  }

  /* Back of card */
  .card-back {
    position: absolute; left: 213px; top: 643px; width: 762px; height: 435px;
    background: var(--white); overflow: hidden;
  }
  .skyline {
    position: absolute; left: 0; right: 0; bottom: 0; height: 190px;
    background: linear-gradient(to bottom, rgba(236,237,237,0) 0%, var(--skyline) 35%, var(--skyline) 100%);
  }
  .portrait {
    position: absolute; left: 400px; top: 28px; width: 362px; height: 407px;
    background: linear-gradient(to right, rgba(255,255,255,0) 0%, #c9a48f 22%, #8a5a44 50%, #d7b9a5 72%, #f3efe9 100%);
    border-radius: 140px 140px 0 0;
  }
  .brand-back {
    position: absolute; left: 46px; top: 50px; width: 250px;
    color: var(--red); font-weight: 700; line-height: 1; text-align: center;
  }
  .brand-back .brand-main { display: block; font-size: 64px; letter-spacing: 1px; }
  .brand-back .brand-sub { display: block; font-size: 20px; letter-spacing: 5px; margin-top: 10px; padding-left: 5px; }
  .name-band {
    position: absolute; left: 0; top: 184px; width: 500px; height: 68px;
    background: linear-gradient(to right, var(--red) 0%, var(--red) 45%, var(--red-soft) 62%, var(--pink) 80%, rgba(248,211,212,0) 100%);
    color: var(--white); padding: 9px 0 0 46px;
  }
  .agent-name { font-weight: 800; font-size: 30px; letter-spacing: 1px; line-height: 1; }
  .agent-title { font-weight: 500; font-size: 17px; letter-spacing: 0.6px; margin-top: 6px; }
  .address {
    position: absolute; left: 47px; top: 255px; font-style: normal;
    color: var(--ink); font-size: 17.5px; letter-spacing: 0.6px; line-height: 28px;
  }
  .divider { position: absolute; left: 47px; top: 311px; width: 58px; height: 3px; background: var(--red); }
  .contacts {
    position: absolute; left: 46px; top: 318px; list-style: none;
    color: var(--ink); font-size: 17.5px; letter-spacing: 0.6px;
  }
  .contacts li { display: flex; align-items: center; gap: 8px; height: 29px; }
  .contacts svg { width: 15px; height: 15px; fill: var(--red); flex: none; }
</style>
</head>
<body>
<main class="canvas">
  <section class="card-front" aria-label="Business card front">
    <div class="pattern" role="img" aria-label="Subtle repeating sparkle pattern on red"></div>
    <div class="brand-front"><span class="brand-main">EMBER</span><span class="brand-sub">REALTY CO</span></div>
    <p class="front-url">www.emberrealtyco.com</p>
  </section>

  <section class="card-back" aria-label="Business card back">
    <div class="skyline" role="img" aria-label="Faint city skyline illustration"></div>
    <div class="portrait" role="img" aria-label="Portrait photo of the broker associate"></div>
    <div class="brand-back"><span class="brand-main">EMBER</span><span class="brand-sub">REALTY CO</span></div>
    <div class="name-band">
      <h1 class="agent-name">DANA MORROW</h1>
      <p class="agent-title">Broker Associate</p>
    </div>
    <address class="address">
      214 Harbor Point Suite<br>Marina Business Quarter
    </address>
    <div class="divider"></div>
    <ul class="contacts">
      <li>
        <svg viewBox="0 0 24 24" aria-hidden="true"><path d="M6.6 10.8a15.1 15.1 0 0 0 6.6 6.6l2.2-2.2a1 1 0 0 1 1-.25 11.4 11.4 0 0 0 3.6.57 1 1 0 0 1 1 1V20a1 1 0 0 1-1 1A17 17 0 0 1 3 4a1 1 0 0 1 1-1h3.5a1 1 0 0 1 1 1c0 1.25.2 2.45.57 3.570a1 1 0 0 1-.25 1z"/></svg>
        401-555-0148
      </li>
      <li>
        <svg viewBox="0 0 24 24" aria-hidden="true"><path d="M2 5h20v14H2z M2 5l10 8 10-8" fill="none" stroke="#e2382a" stroke-width="2.4"/></svg>
        hello@emberrealtyco.com
      </li>
      <li>
        <svg viewBox="0 0 24 24" aria-hidden="true"><g fill="none" stroke="#e2382a" stroke-width="2"><circle cx="12" cy="12" r="9.5"/><ellipse cx="12" cy="12" rx="4" ry="9.5"/><path d="M2.5 12h19M4 7h16M4 17h16"/></g></svg>
        www.emberrealtyco.com
      </li>
    </ul>
  </section>
</main>
</body>
</html>
```